**Designs Wanted for High Profile Banner Ad Campaign**

Our leading Public Relations agency services some of the world's leading brands in our local market.

We now need a banner ad design to support our own growth.

We are looking to have banner ads designed that will carry a common theme to be used across the following sizes (all these sizes will need to be created):
• Vertical rectangle: 240 x 400
• Mobile leaderboard: 320 x 50
• Banner: 468 x 60
• Leaderboard: 728 x 90
• Square: 250 x 250
• Small square: 200 x 200
• Large rectangle: 336 x 280
• Inline rectangle: 300 x 250
• Skyscraper: 120 x 600
• Wide skyscraper: 160 x 600
• Half-page: 300 x 600
• Large leaderboard: 970x90
• Large mobile banner: 320 x 100
• Billboard: 970 x 250

Our primary retargeting and regular display campaign objective is to encourage marketing managers and business owners to visit our site and contact us.
See www.lumenvoicecomms.co.nz for our current look and feel. Please keep consistent colours with that site. Our two logos are attached.

This is our first digital retargeting campaign and we are open to your advice and suggestions on what will encourage click through from potential clients.

Our current thinking at the moment is that the ad could be built around these concepts:
“Reach, socialise, inspire.”
In others words – as a PR agency we help clients ‘reach’ their target market through creating content for news media.
The ‘socialise’ represents engagement through social media – in that we help develop and build their social media presence.
‘Inspire’ refers to the fact we aim to inspire their target market towards engaging with our clients.
Plus a suitable call to action– eg. Click here to meet your public relations needs today.

In terms of designs we are open to suggestion: eg. the adverts could use icons or something else that you have seen work.

We would like to see some eye catching animation, interaction or movement in the advert to.

We need the ad to be effective, eye catching, professional, modern, sophisticated (in that our target market is professional executives) and crisp, clean and uncluttered.

Time is short for us, so please send through designs as soon as possible – don’t wait until the last day!

Additional note: the existing fish image and 'stand out from the crowd' slogan on our home page are not required as part of this design. We have been looking to move towards the new slogan (“Reach, socialise, inspire.” ) and this banner ad may also serve to give us some new direction ideas as well. we do need to keep the existing logo and orange colour though.

Target Market(s)

Business to Business. Marketing and brand managers, Small, Medium and large business owners and executives.
Those with a business in the New Zealand market.

Industry/Entity Type

Marketing

Requirements
Must have
• our logo
animation or movement
orange colour/ consistency with our existing website.
our proposed slogan: “Reach, socialise, inspire.” (however we are open to seeing alternative ideas as well if you want to submit more than one concept)
call to action.
Should not have
• read note about existing fish and slogan above.

```html
<!DOCTYPE html>
<html lang="en">
<head>
<meta charset="utf-8">
<title>Lumenvoice – Discover the Power of Public Relations</title>
<link rel="stylesheet" href="https://fonts.googleapis.com/css2?family=Raleway:wght@300&family=Lato:wght@300;400&family=Tinos&display=swap">
<style>
  :root {
    --page-bg: #ffffff;
    --frame: #1a1a1a;
    --logo-grey: #4a4a4a;
    --brand-orange: #e8672a;
    --brand-orange-deep: #c8521b;
    --desk-light: #4a4a4a;
    --desk-mid: #2e2e2e;
    --desk-dark: #161616;
    --ink-light: #ffffff;
    --caption-ink: #111111;
  }
  html, body {
    margin: 0;
    padding: 0;
    width: 1200px;
    height: 979px;
    overflow: hidden;
    background: var(--page-bg);
  }
  .canvas {
    position: relative;
    width: 1200px;
    height: 979px;
  }
  .banner {
    position: absolute;
    left: 153px;
    top: 81px;
    width: 900px;
    height: 750px;
    box-sizing: border-box;
    border: 3px solid var(--frame);
    overflow: hidden;
    background: var(--page-bg);
  }
  .brand-bar {
    position: absolute;
    left: 0;
    top: 0;
    width: 100%;
    height: 204px;
    display: flex;
    align-items: center;
    justify-content: center;
  }
  .brand-name {
    font-family: "Raleway", sans-serif;
    font-weight: 300;
    font-size: 118px;
    letter-spacing: 4px;
    line-height: 1;
    color: var(--logo-grey);
  }
  .hero {
    position: absolute;
    left: 0;
    top: 204px;
    width: 100%;
    height: 546px;
  }
  .hero-backdrop {
    position: absolute;
    inset: 0;
    background:
      radial-gradient(ellipse at 30% 25%, var(--desk-light) 0%, transparent 55%),
      radial-gradient(ellipse at 85% 80%, var(--desk-light) 0%, transparent 45%),
      linear-gradient(160deg, var(--desk-mid) 0%, var(--desk-dark) 100%);
  }
  .headline {
    position: absolute;
    left: 0;
    top: 118px;
    width: 100%;
    margin: 0;
    text-align: center;
    font-family: "Lato", sans-serif;
    font-weight: 300;
    font-size: 56px;
    line-height: 75px;
    letter-spacing: 1px;
    color: var(--ink-light);
    text-transform: uppercase;
  }
  .pointer-arrow {
    position: absolute;
    left: 680px;
    top: 276px;
    width: 90px;
    height: 120px;
  }
  .cta-button {
    position: absolute;
    left: 231px;
    top: 363px;
    width: 426px;
    height: 90px;
    box-sizing: border-box;
    display: flex;
    align-items: center;
    justify-content: center;
    gap: 22px;
    border-radius: 6px;
    background: linear-gradient(180deg, var(--brand-orange) 0%, var(--brand-orange-deep) 100%);
    color: var(--ink-light);
    font-family: "Lato", sans-serif;
    font-weight: 400;
    font-size: 40px;
    letter-spacing: 3px;
    text-decoration: none;
    text-transform: uppercase;
  }
  .cta-icon {
    width: 50px;
    height: 50px;
  }
  .file-size {
    position: absolute;
    left: 0;
    top: 888px;
    width: 100%;
    margin: 0;
    text-align: center;
    font-family: "Tinos", serif;
    font-size: 40px;
    color: var(--caption-ink);
  }
</style>
</head>
<body>
<div class="canvas">
  <section class="banner">
    <header class="brand-bar">
      <span class="brand-name">LUMENVOICE</span>
    </header>
    <div class="hero">
      <div class="hero-backdrop" role="img" aria-label="Dark overhead photograph of a working desk with laptop, keyboard, coffee cup and hands"></div>
      <h1 class="headline">Discover the power of<br>public relations</h1>
      <svg class="pointer-arrow" viewBox="0 0 90 120" aria-hidden="true">
        <path d="M70 6 C 78 50, 60 88, 22 108" fill="none" stroke="#ffffff" stroke-width="6" stroke-linecap="round"/>
        <path d="M20 84 L 20 110 L 46 112" fill="none" stroke="#ffffff" stroke-width="6" stroke-linecap="round" stroke-linejoin="round"/>
      </svg>
      <a class="cta-button" href="#">
        <span>Learn more</span>
        <svg class="cta-icon" viewBox="0 0 50 50" aria-hidden="true">
          <circle cx="25" cy="25" r="23" fill="#ffffff"/>
          <path d="M20 14 L31 25 L20 36" fill="none" stroke="#c8521b" stroke-width="7" stroke-linecap="round" stroke-linejoin="round"/>
        </svg>
      </a>
    </div>
  </section>
  <p class="file-size">file size 64kb</p>
</div>
</body>
</html>
```